Karvel Wordcraft web design: a translation company with corporate clients

Need a new website for my translation and localization company with file uploading capacity directed to email for quotation

old (very old) web site is www.tpxyazilar.com you can use the content text there or lorem ipsum, We will provide the texts. It will be in English - Turkish - French and German
For the content and overall layout: https://www.plomvinlanguage.com/

For the color scheme you'll need to see logo's colors.

I am rebranding so new logo is uploaded The new adress will be www.karvelwordcraft.com

Target Market(s)

Primarily corporate clients

Industry/Entity Type

It Company

Coding

Coded - Design and coding required

Number of Pages Required

5+ page

Font styles to use
Other font styles liked:
• Calibri

Requirements
Must have
• References on homepage (logos will be sent during design phase)
• Services: Translation, Interpretation, Localization&Consultancy, Translation API
• Quotation Form and file uploading
• Simple layout evoking reliability, speed and accuracy
Nice to have
• For the content and overall layout: https://www.plomvinlanguage.com/
• Separate page for Translation Services: Marketing Translation, Legal Translation, Technical Translation, Personal Translation
• and texts under these headings
Should not have
• Old style
• Complex design

```html
<!DOCTYPE html>
<html lang="en">
<head>
<meta charset="utf-8">
<title>Karvel Wordcraft — Translation, Localization &amp; Consultancy</title>
<link href="https://fonts.googleapis.com/css2?family=Open+Sans:wght@400;600;700;800&display=swap" rel="stylesheet">
<style>
:root{
  --green:#4a6024;
  --green-dark:#3d561c;
  --green-deep:#334a17;
  --orange:#f7941d;
  --ink:#333;
  --muted:#666;
  --line:#e3e3e3;
  --panel:#f3f4f6;
  --footer:#2b2b2b;
}
*{box-sizing:border-box;margin:0;padding:0}
html,body{width:1200px;height:2835px;overflow:hidden}
body{font-family:"Open Sans",Arial,sans-serif;color:var(--ink);background:#fff;position:relative}
a{color:inherit;text-decoration:none}

/* top bar */
.topbar{height:26px;background:var(--green);color:#fff;font-size:10px;display:flex;align-items:center;padding:0 160px;white-space:nowrap}
.topbar .lang{display:flex;align-items:center;gap:6px}
.topbar .flag{width:16px;height:10px;background:#c9d3e6;display:inline-block}
.topbar .right{margin-left:auto;display:flex;align-items:stretch;height:26px}
.topbar .right span{display:flex;align-items:center;gap:6px;padding:0 16px;border-left:1px solid rgba(255,255,255,.25)}
.topbar .right span:last-child{padding-right:0}

/* header */
.header{height:109px;background:linear-gradient(#fff,#f1f1f1);display:flex;align-items:center;padding:0 160px;border-bottom:1px solid #ddd;white-space:nowrap}
.logo{display:flex;align-items:center;gap:10px}
.logo .mark{width:34px;height:34px;border-radius:50%;background:var(--orange);flex:none}
.logo .name{font-size:24px;font-weight:600;color:var(--green);line-height:1}
.logo .tag{font-size:7px;color:var(--green);letter-spacing:.3px;margin-top:4px}
.nav{margin-left:auto;display:flex;align-items:center;gap:26px;font-size:12px;color:var(--green-deep)}
.nav a{white-space:nowrap}
.nav .active{border-bottom:2px solid var(--orange);padding:4px 0}
.nav .quote{background:var(--orange);color:#fff;font-size:10px;padding:0 22px;height:30px;line-height:30px;border-radius:2px;margin-left:14px}

/* hero */
.hero{position:relative;height:479px;overflow:hidden;background:radial-gradient(ellipse at 30% 40%,#f3f0df 0%,#e2e6cf 55%,#d6dcc0 100%)}
.hero .map{position:absolute;left:180px;top:40px;width:600px;height:320px;border-radius:50%;background:radial-gradient(ellipse,rgba(120,135,100,.18),rgba(120,135,100,0) 70%)}
.hero h1{position:absolute;left:160px;top:160px;font-size:38px;font-weight:800;line-height:56px;letter-spacing:-.3px}
.hero h1 .o{color:var(--orange);display:block}
.hero h1 .g{color:var(--green-dark);display:block}
.hero .art{position:absolute;left:690px;top:14px;width:330px;height:440px;border-radius:160px;background:radial-gradient(circle at 60% 45%,#dbe6f0 0%,#c9d6de 45%,rgba(210,215,200,0) 72%)}
.dots{position:absolute;left:584px;top:448px;display:flex;gap:5px}
.dots i{width:9px;height:9px;border-radius:50%;border:1.5px solid #555;display:block}
.dots i.on{background:#555}

/* blog ticker */
.ticker{height:71px;background:#f6f7f9;border-bottom:1px solid var(--line);display:flex;align-items:center;padding:0 231px;font-size:10px;color:#333;white-space:nowrap}
.ticker .badge{background:var(--orange);color:#fff;font-weight:700;font-size:9px;padding:5px 14px;margin-right:20px;border-radius:2px}
.ticker .more{margin-left:auto;color:var(--orange);font-weight:600;font-size:9px;display:flex;align-items:center;gap:6px}

/* section titles */
.title{text-align:center;color:var(--green-dark);font-weight:800;font-size:28px;letter-spacing:.2px}
.sub{text-align:center;font-size:13px;color:#444;margin-top:6px}

/* services */
.services{height:338px;padding-top:42px;border-bottom:1px solid var(--line)}
.services .lead{width:780px;margin:8px auto 0;text-align:center;font-size:13px;font-weight:600;color:#555;line-height:19px}
.cards{position:relative;display:flex;gap:25px;padding:0 160px;margin-top:24px}
.card{width:201px;height:144px;position:relative;display:flex;align-items:center;justify-content:center;text-align:center;color:#fff;font-size:14px;text-shadow:0 1px 2px rgba(0,0,0,.5)}
.card.t1{background:linear-gradient(135deg,#1f4f86,#3a7fb8 55%,#1c3f70)}
.card.t2{background:linear-gradient(135deg,#6d6d6d,#9b9b9b 50%,#5a5a5a)}
.card.t3{background:linear-gradient(135deg,#1d3350,#4b6a86 55%,#22364d)}
.card.t4{background:linear-gradient(135deg,#2f6fb5,#6aa7e0 55%,#2a5a96)}
.card .arr{position:absolute;top:62px;width:20px;height:20px;border-radius:50%;background:rgba(255,255,255,.85)}
.card .arr.l{left:6px}.card .arr.r{right:6px}

/* clients */
.clients{height:240px;padding-top:52px}
.clients .title{display:flex;align-items:center;justify-content:center;gap:10px}
.logos{display:flex;justify-content:space-between;align-items:center;padding:0 160px;margin-top:30px;white-space:nowrap}
.client{display:flex;align-items:center;gap:8px;font-size:24px;font-weight:700;color:#1f2a5c}
.client .sq{width:20px;height:20px;background:#1f2a5c}

/* quote form */
.quote{height:686px;background:var(--panel);padding-top:44px}
.quote .sub{font-size:12px;margin-top:4px}
.steps{position:relative;margin:30px 160px 0;height:74px}
.steps .bar{position:absolute;top:22px;left:0;right:0;height:4px;background:var(--green-deep)}
.steps .bar.done{right:auto;width:276px;background:var(--orange)}
.step{position:absolute;top:10px;width:200px;margin-left:-100px;text-align:center}
.step .num{width:26px;height:26px;border-radius:50%;background:var(--green-deep);color:#fff;font-size:11px;font-weight:700;line-height:26px;margin:0 auto;border:3px solid var(--panel);box-sizing:content-box;margin-top:-3px}
.step.now .num{background:var(--orange)}
.step .lbl{font-size:11px;font-weight:700;color:#222;margin-top:8px}
.step.now .lbl{color:var(--orange)}
.form{display:block;margin:0 160px;background:#fff;height:444px;padding:24px 24px}
.row{display:flex;gap:24px}
.field{flex:1}
.field label{display:block;font-size:10px;font-weight:700;color:var(--green-dark);margin-bottom:10px}
.select{height:38px;border:1px solid #ddd;border-radius:3px;display:flex;align-items:center;padding:0 12px;font-size:10px;color:#555;gap:8px}
.select .chev{margin-left:auto}
.gap{height:22px}
.lists{display:flex;align-items:center;gap:14px}
.list{width:406px;height:142px;border:1px solid #ddd;border-radius:3px;padding:8px 14px;font-size:10px;color:#444;line-height:26px;position:relative}
.list .scroll{position:absolute;right:3px;top:4px;bottom:4px;width:9px;background:#f0f0f0;border:1px solid #ddd}
.swap{font-size:11px;color:#555}
.next{display:block;width:128px;height:34px;margin:22px auto 0;background:var(--orange);color:#fff;font-size:11px;font-weight:700;text-align:center;line-height:34px;border-radius:2px}

/* who we are */
.who{height:278px;padding-top:42px}
.who .sub{font-size:12px;margin-top:2px}
.cols{display:flex;padding:0 160px;margin-top:28px;gap:47px}
.col{width:262px}
.col h3{font-size:15px;font-weight:600;color:var(--orange)}
.col p{font-size:11px;line-height:18px;color:#444;margin-top:6px}
.btn{display:inline-block;border:1px solid #ccc;font-size:10px;padding:4px 18px;margin-top:12px;color:#333;background:#fff}

/* blog */
.blog{height:437px;background:var(--green);padding-top:42px}
.blog .title{color:#fff}
.blog .sub{color:#e8ecdf;font-size:12px;margin-top:2px}
.posts{display:flex;gap:26px;padding:0 160px;margin-top:20px}
.post{width:277px;height:279px;background:#fff;padding:6px}
.post .img{height:131px}
.post .img.p1{background:linear-gradient(135deg,#cfd8e3,#8fa4bd 60%,#5c6f86)}
.post .img.p2{background:linear-gradient(135deg,#e6e0d4,#b9ad98 60%,#7c705e)}
.post .img.p3{background:linear-gradient(135deg,#d9d6d0,#9a958c 60%,#4d4a45)}
.meta{display:flex;align-items:center;font-size:10px;color:#333;margin-top:8px;padding:0 2px}
.meta span{display:flex;align-items:center;gap:5px}
.meta span + span{margin-left:auto}
.post h4{font-size:11px;font-weight:700;color:var(--orange);margin-top:10px}
.post p{font-size:10px;line-height:16px;color:#444;margin-top:3px}
.post .btn{margin-top:8px}

/* footer */
.footer{height:171px;background:var(--footer);color:#ddd;text-align:center;padding-top:36px}
.footer .links{display:flex;justify-content:center;gap:24px;font-size:11px;letter-spacing:.3px}
.social{display:flex;justify-content:center;gap:12px;margin-top:22px}
.social i{width:30px;height:30px;border-radius:50%;background:#fff;display:block}
.copy{font-size:10px;margin-top:16px;color:#ccc}
</style>
</head>
<body>

<div class="topbar">
  <div class="lang">Change Language <span class="flag"></span>
    <svg width="8" height="6" viewBox="0 0 8 6"><path d="M1 1l3 3 3-3" stroke="#fff" stroke-width="1.5" fill="none"/></svg>
  </div>
  <div class="right">
    <span><svg width="10" height="10" viewBox="0 0 24 24"><path fill="var(--orange)" d="M6.6 10.8a15 15 0 0 0 6.6 6.6l2.2-2.2c.3-.3.7-.4 1-.2 1.1.4 2.3.6 3.6.6.6 0 1 .4 1 1V20c0 .6-.4 1-1 1A17 17 0 0 1 3 4c0-.6.4-1 1-1h3.5c.6 0 1 .4 1 1 0 1.3.2 2.5.6 3.6.1.3 0 .7-.2 1z"/></svg>+00 4410 5620 18</span>
    <span>REGISTER</span>
    <span>LOG IN</span>
    <span>LIVE CHAT</span>
  </div>
</div>

<header class="header">
  <div class="logo">
    <div class="mark"></div>
    <div>
      <div class="name">Karvel Wordcraft</div>
      <div class="tag">TRANSLATION, LOCALIZATION &amp; CONSULTANCY</div>
    </div>
  </div>
  <nav class="nav">
    <a class="active">Translation Services</a>
    <a>Languages</a>
    <a>Resources</a>
    <a>Pricing</a>
    <a>About Us</a>
    <a>Blog</a>
    <a class="quote">GET A QUOTE</a>
  </nav>
</header>

<section class="hero">
  <div class="map" role="img" aria-label="Faint world map in the background"></div>
  <h1><span class="o">DELIVERY ON TIME</span><span class="g">WITH PERFECT QUALITY</span></h1>
  <div class="art" role="img" aria-label="Illustration of a translator with circles for time, delivery and quality"></div>
  <div class="dots"><i class="on"></i><i></i><i></i></div>
</section>

<div class="ticker">
  <span class="badge">BLOG</span>
  Lorem ipsum dolor sit amet, consectetur adipiscing elit, sed do eiusmod tempor incididunt ut labore et dolore magna aliqua.
  <span class="more">READ MORE <svg width="7" height="10" viewBox="0 0 7 10"><path d="M1 1l4 4-4 4" stroke="var(--orange)" stroke-width="2" fill="none"/></svg></span>
</div>

<section class="services">
  <h2 class="title">PROFESSIONAL TRANSLATION SERVICES</h2>
  <p class="lead">Lorem ipsum dolor sit amet, consectetur adipiscing elit, sed do eiusmod tempor incididunt ut labore et dolore magna aliqua Ut enim ad minim veniamquis.</p>
  <div class="cards">
    <div class="card t1" role="img" aria-label="Blue binary code photo for Translation"><span class="arr l"></span>Translation</div>
    <div class="card t2" role="img" aria-label="Dictionary page photo for Interpretation">Interpretation</div>
    <div class="card t3" role="img" aria-label="Globe photo for Localization and Consultancy">Localization&amp;<br>Consultancy</div>
    <div class="card t4" role="img" aria-label="Network graphic photo for Translation API">Translation API<span class="arr r"></span></div>
  </div>
</section>

<section class="clients">
  <h2 class="title">
    <svg width="20" height="20" viewBox="0 0 20 20"><circle cx="10" cy="10" r="9" fill="var(--green-dark)"/><path d="M12 5l-5 5 5 5" stroke="#fff" stroke-width="2.4" fill="none"/></svg>
    OUR CLIENTS
    <svg width="20" height="20" viewBox="0 0 20 20"><circle cx="10" cy="10" r="9" fill="var(--orange)"/><path d="M8 5l5 5-5 5" stroke="#fff" stroke-width="2.4" fill="none"/></svg>
  </h2>
  <p class="sub" style="font-weight:600">Delivery On Time With Perfect Quality</p>
  <div class="logos">
    <div class="client">Velora Energy</div>
    <div class="client">Tessan Capital <span class="sq"></span></div>
    <div class="client">Norvik University</div>
    <div class="client">Halden &amp; Brisk</div>
  </div>
</section>

<section class="quote">
  <h2 class="title">TRANSLATION QUOTE FORM</h2>
  <p class="sub">As easy as 1, 2, 3...</p>
  <div class="steps">
    <div class="bar"></div><div class="bar done"></div>
    <div class="step now" style="left:138px"><div class="num">1</div><div class="lbl">TIME &amp; LANGUAGES</div></div>
    <div class="step" style="left:440px"><div class="num">2</div><div class="lbl">UPLOAD FILES</div></div>
    <div class="step" style="left:740px"><div class="num">3</div><div class="lbl">YOUR INFO</div></div>
  </div>
  <form class="form">
    <div class="row">
      <div class="field"><label>Timeframe</label>
        <div class="select"><svg width="12" height="12" viewBox="0 0 12 12"><circle cx="6" cy="6" r="5" stroke="#999" fill="none"/><path d="M6 3v3h2" stroke="#999" fill="none"/></svg>Express (within 48 hours)<svg class="chev" width="10" height="7" viewBox="0 0 10 7"><path d="M1 1l4 4 4-4" stroke="#333" stroke-width="1.8" fill="none"/></svg></div>
      </div>
      <div class="field"><label>Certification</label>
        <div class="select"><svg width="12" height="12" viewBox="0 0 12 12"><circle cx="6" cy="6" r="5" stroke="#999" fill="none"/><path d="M6 3v3h2" stroke="#999" fill="none"/></svg>Not Required<svg class="chev" width="10" height="7" viewBox="0 0 10 7"><path d="M1 1l4 4 4-4" stroke="#333" stroke-width="1.8" fill="none"/></svg></div>
      </div>
    </div>
    <div class="gap"></div>
    <div class="field"><label>Translate From</label>
      <div class="select"><svg width="12" height="12" viewBox="0 0 12 12"><circle cx="6" cy="6" r="5" stroke="#999" fill="none"/><path d="M6 3v3h2" stroke="#999" fill="none"/></svg>English<svg class="chev" width="10" height="7" viewBox="0 0 10 7"><path d="M1 1l4 4 4-4" stroke="#333" stroke-width="1.8" fill="none"/></svg></div>
    </div>
    <div class="gap"></div>
    <div class="field"><label>Translate To</label>
      <div class="lists">
        <div class="list">Arabic<br>Chinese Simplified<br>Chinese Traditional<br>English<br>English (USA)<span class="scroll"></span></div>
        <span class="swap">⇄</span>
        <div class="list"></div>
      </div>
    </div>
    <a class="next">NEXT</a>
  </form>
</section>

<section class="who">
  <h2 class="title">WHO WE ARE</h2>
  <p class="sub">Lorem ipsum dolor sit amet</p>
  <div class="cols">
    <div class="col"><h3>In the News</h3><p>Lorem ipsum dolor sit amet, consectetur adipiscing elit, sed do eiusmod tempor incididunt ut labore et dolore magna aliqua.</p><a class="btn">Read More</a></div>
    <div class="col"><h3>Why Choose Us</h3><p>Lorem ipsum dolor sit amet, consectetur adipiscing elit, sed do eiusmod tempor incididunt ut labore et dolore magna aliqua.</p><a class="btn">Read More</a></div>
    <div class="col"><h3>About Us</h3><p>Lorem ipsum dolor sit amet, consectetur adipiscing elit, sed do eiusmod tempor incididunt ut labore et dolore magna aliqua.</p><a class="btn">Read More</a></div>
  </div>
</section>

<section class="blog">
  <h2 class="title">RECENT BLOG POSTS</h2>
  <p class="sub">Lorem Ipsum Dolor Sit Amet</p>
  <div class="posts">
    <article class="post">
      <div class="img p1" role="img" aria-label="Photo of hands typing on a laptop"></div>
      <div class="meta"><span><svg width="11" height="11" viewBox="0 0 12 12"><rect x="1" y="2" width="10" height="9" fill="#333"/><rect x="2" y="5" width="8" height="5" fill="#fff"/></svg>06 Mar 2016</span><span><svg width="12" height="10" viewBox="0 0 12 10"><path d="M1 1h10v6H5l-3 2V7H1z" fill="#333"/></svg>Comments(5)</span></div>
      <h4>Lorem ipsum dolor sit amet</h4>
      <p>Lorem ipsum dolor sit amet, consectetur adipiscing elit, sed do eiusmod tempor incididunt ut labore et dolore magna aliqua.</p>
      <a class="btn">Read More</a>
    </article>
    <article class="post">
      <div class="img p2" role="img" aria-label="Photo of a hand writing on documents"></div>
      <div class="meta"><span><svg width="11" height="11" viewBox="0 0 12 12"><rect x="1" y="2" width="10" height="9" fill="#333"/><rect x="2" y="5" width="8" height="5" fill="#fff"/></svg>07 Mar 2016</span><span><svg width="12" height="10" viewBox="0 0 12 10"><path d="M1 1h10v6H5l-3 2V7H1z" fill="#333"/></svg>Comments(3)</span></div>
      <h4>Lorem ipsum dolor sit amet</h4>
      <p>Lorem ipsum dolor sit amet, consectetur adipiscing elit, sed do eiusmod tempor incididunt ut labore et dolore magna aliqua.</p>
      <a class="btn">Read More</a>
    </article>
    <article class="post">
      <div class="img p3" role="img" aria-label="Photo of an office desk with a phone and computer"></div>
      <div class="meta"><span><svg width="11" height="11" viewBox="0 0 12 12"><rect x="1" y="2" width="10" height="9" fill="#333"/><rect x="2" y="5" width="8" height="5" fill="#fff"/></svg>08 Mar 2016</span><span><svg width="12" height="10" viewBox="0 0 12 10"><path d="M1 1h10v6H5l-3 2V7H1z" fill="#333"/></svg>Comments(2)</span></div>
      <h4>Lorem ipsum dolor sit amet</h4>
      <p>Lorem ipsum dolor sit amet, consectetur adipiscing elit, sed do eiusmod tempor incididunt ut labore et dolore magna aliqua.</p>
      <a class="btn">Read More</a>
    </article>
  </div>
</section>

<footer class="footer">
  <nav class="links">
    <a>TRANSLATION SERVICES</a><a>LANGUAGES</a><a>RESOURCES</a><a>PRICING</a><a>ABOUT US</a><a>BLOG</a>
  </nav>
  <div class="social"><i></i><i></i><i></i><i></i></div>
  <p class="copy">Copyright © 2016 karvelwordcraft.com. All Rights Reserved.</p>
</footer>

</body>
</html>
```